Newly established winery needs label for its bottles

The Corvel-Tamarin Winery, is a small family owned winery that has been producing wine for little over 3 years. We are now ready to officially start commercializing our products. To do so we are looking for a label for our wine bottles. We are looking for a creative design that will differentiate our bottles from the more conventional labels. We are looking for one label design with 3 color schemes so that we can have a standard look and feel for all three of our wines, while having some differentiation between them with the different color schemes. In summary we are looking for a label that will standout by its uniqueness, simplicity and its modern touch. The label should also reflect the historical significance of the name of the winery. The attached documents offers more detail about the winery, what we are looking for, as well as some technical specification for the label. This label project is also related to a logo project see brief: http://www.pitchvault.ca/project-progress.aspx?briefId=462193). The logo project is now complete and the winning design source files were added to the documents in this brief. Also, details around the information that will need to appear on the label was added to the document list.
Updates
This label project will be on hold temporarily while the logo project is in progress. If you are interested in participating in the logo project, please follow this link: http://www.pitchvault.ca/project-progress.aspx?briefId=462193 Added Wednesday, December 17, 2014
Reason: Deadline extended to give sufficent time for submission and modification to the designs provided.

```html
<!DOCTYPE html>
<html lang="en">
<head>
<meta charset="utf-8">
<title>Corvel Tamarin — Wine Labels</title>
<link href="https://fonts.googleapis.com/css2?family=Cormorant+Garamond:ital,wght@0,500;1,500&family=Josefin+Sans:wght@300;400&display=swap" rel="stylesheet">
<style>
  :root {
    --backdrop: #78716a;
    --paper: #ffffff;
    --brand-ink: #9a6630;
    --fine-ink: #3b3b3b;

    --white-field: #d6e83c;
    --white-field-deep: #c4dc2a;
    --white-text: #3d8c2c;
    --white-art: #b9d133;

    --rose-field: #f25a8e;
    --rose-field-deep: #e9477d;
    --rose-text: #ffe1ea;
    --rose-art: #e0427a;

    --red-field: #d52c40;
    --red-field-deep: #c72136;
    --red-text: #fbd0cf;
    --red-art: #b81f33;
  }

  * { box-sizing: border-box; margin: 0; padding: 0; }

  html, body {
    width: 1200px;
    height: 871px;
    overflow: hidden;
    background: var(--backdrop);
  }

  .label-range {
    width: 1200px;
    height: 871px;
    display: flex;
    justify-content: center;
    align-items: center;
    gap: 60px;
  }

  .wine-label {
    width: 300px;
    height: 512px;
    display: flex;
    flex-direction: column;
    background: var(--paper);
    box-shadow: 0 6px 18px rgba(0, 0, 0, 0.22);
  }

  .label-header {
    height: 126px;
    display: flex;
    flex-direction: column;
    align-items: center;
    justify-content: center;
    gap: 6px;
  }

  .brand-row {
    display: flex;
    align-items: center;
    gap: 12px;
  }

  .brand-tag {
    font-family: "Josefin Sans", sans-serif;
    font-weight: 400;
    font-size: 7px;
    letter-spacing: 1.2px;
    color: var(--brand-ink);
    text-transform: uppercase;
    line-height: 1.3;
    border-top: 1px solid var(--brand-ink);
    border-bottom: 1px solid var(--brand-ink);
    padding: 2px 0;
  }

  .brand-tag.tag-left { text-align: right; }

  .brand-mark {
    width: 14px;
    height: 14px;
    border-radius: 50%;
    background: var(--brand-ink);
  }

  .brand-name {
    font-family: "Cormorant Garamond", serif;
    font-weight: 500;
    font-size: 19px;
    letter-spacing: 3px;
    color: var(--brand-ink);
    text-transform: uppercase;
    line-height: 1;
  }

  .label-field {
    height: 322px;
    display: flex;
    flex-direction: column;
    align-items: center;
    padding-top: 26px;
    background: linear-gradient(90deg, var(--field-deep) 0%, var(--field) 30%, var(--field) 70%, var(--field-deep) 100%);
    color: var(--field-text);
  }

  .wine-name {
    font-family: "Josefin Sans", sans-serif;
    font-weight: 300;
    font-size: 28px;
    letter-spacing: 0.5px;
    line-height: 1;
    text-transform: uppercase;
  }

  .origin {
    font-family: "Cormorant Garamond", serif;
    font-style: italic;
    font-weight: 500;
    font-size: 14px;
    margin-top: 4px;
  }

  .vineyard-scene {
    width: 196px;
    height: 110px;
    margin: 14px 0 20px;
    border-radius: 4px;
    background: radial-gradient(ellipse at 50% 60%, var(--art) 0%, transparent 75%);
  }

  .label-footer {
    height: 64px;
    display: flex;
    align-items: center;
    justify-content: space-between;
    padding: 0 52px 0 48px;
    font-family: "Josefin Sans", sans-serif;
    font-weight: 400;
    font-size: 11px;
    color: var(--fine-ink);
  }

  .label-white { --field: var(--white-field); --field-deep: var(--white-field-deep); --field-text: var(--white-text); --art: var(--white-art); }
  .label-rose  { --field: var(--rose-field);  --field-deep: var(--rose-field-deep);  --field-text: var(--rose-text);  --art: var(--rose-art); }
  .label-red   { --field: var(--red-field);   --field-deep: var(--red-field-deep);   --field-text: var(--red-text);   --art: var(--red-art); }
</style>
</head>
<body>
<main class="label-range">

  <article class="wine-label label-white">
    <header class="label-header">
      <div class="brand-row">
        <span class="brand-tag tag-left">Vignoble<br>Familial</span>
        <span class="brand-mark"></span>
        <span class="brand-tag tag-right">Family<br>Winery</span>
      </div>
      <p class="brand-name">Corvel Tamarin</p>
    </header>
    <section class="label-field">
      <h2 class="wine-name">White Wine</h2>
      <p class="origin">Product of Québec</p>
      <div class="vineyard-scene" role="img" aria-label="Line sketch of a hillside vineyard with rows of vines and a farmhouse"></div>
      <h2 class="wine-name">Vin Blanc</h2>
      <p class="origin">Produit du Québec</p>
    </section>
    <footer class="label-footer">
      <span class="abv">11.6% alc./Vol.</span>
      <span class="volume">750 ml</span>
    </footer>
  </article>

  <article class="wine-label label-rose">
    <header class="label-header">
      <div class="brand-row">
        <span class="brand-tag tag-left">Vignoble<br>Familial</span>
        <span class="brand-mark"></span>
        <span class="brand-tag tag-right">Family<br>Winery</span>
      </div>
      <p class="brand-name">Corvel Tamarin</p>
    </header>
    <section class="label-field">
      <h2 class="wine-name">Rosé</h2>
      <p class="origin">Product of Québec</p>
      <div class="vineyard-scene" role="img" aria-label="Line sketch of a hillside vineyard with rows of vines and a farmhouse"></div>
      <h2 class="wine-name">Rosé</h2>
      <p class="origin">Produit du Québec</p>
    </section>
    <footer class="label-footer">
      <span class="abv">11.6% alc./Vol.</span>
      <span class="volume">750 ml</span>
    </footer>
  </article>

  <article class="wine-label label-red">
    <header class="label-header">
      <div class="brand-row">
        <span class="brand-tag tag-left">Vignoble<br>Familial</span>
        <span class="brand-mark"></span>
        <span class="brand-tag tag-right">Family<br>Winery</span>
      </div>
      <p class="brand-name">Corvel Tamarin</p>
    </header>
    <section class="label-field">
      <h2 class="wine-name">Red Wine</h2>
      <p class="origin">Product of Québec</p>
      <div class="vineyard-scene" role="img" aria-label="Line sketch of a hillside vineyard with rows of vines and a farmhouse"></div>
      <h2 class="wine-name">Vin Rouge</h2>
      <p class="origin">Produit du Québec</p>
    </section>
    <footer class="label-footer">
      <span class="abv">11.6% alc./Vol.</span>
      <span class="volume">750 ml</span>
    </footer>
  </article>

</main>
</body>
</html>
```